Miel du Matin Immerse in the enchanting flavors of France at Miel du Matin

A menu that is French in style with the Eiffel Tower. A elegant menu that is in rich blue with red or gold trimmings, we are a French Bakey and Cafe

Target Market(s)

30 to 55 people

Industry/Entity Type

Restaurant

Font styles to use
Decorative

Colors
0054AA
0677BA
7BADD7
CADEEF
E8F1F8
EB3D1F
EC4F4E
F09395
F8D3D4
FCEDEE

Requirements
Must have
• the attachment "My Brunch Specials" is the Menu I want you to create, it has all the text, "My Brunch Special Complete" is a word version. The menu size should be 4 1/4 wide by 14 inches long 2 Sided. must have our logo at the top , Make the font larger, because our biggest complaint about our menu is it is hard to read
Nice to have
• I would love to incorporate the Eiffel Tower as a silhouette in the background
Should not have
• I do not want too many pictures or small print

```html
<!DOCTYPE html>
<html lang="en">
<head>
<meta charset="utf-8">
<title>Miel du Matin – Brunch &amp; Drink Specials</title>
<link rel="stylesheet" href="https://fonts.googleapis.com/css2?family=Allura&family=Saira+Condensed:wght@400;600;700&family=Saira+Semi+Condensed:wght@400&display=swap">
<style>
  :root{
    --page:#ffffff;
    --navy:#1d1650;
    --navy-light:#2c2766;
    --tower:#35307a;
    --red:#e8202a;
    --ink:#ffffff;
    --badge:#4d4b6e;
    --icon-bg:#d9d9e3;
  }
  *{box-sizing:border-box;margin:0;padding:0}
  html,body{width:900px;height:1200px;overflow:hidden;background:var(--page)}
  body{position:relative;font-family:"Saira Condensed",sans-serif;color:var(--ink)}
  .panel{position:absolute;top:40px;width:340px;height:1119px;background:var(--navy);overflow:hidden}
  .panel--brunch{left:92px}
  .panel--drinks{left:467px}
  .tower-silhouette{position:absolute;right:-10px;bottom:0;width:250px;height:760px;
    background:linear-gradient(180deg,rgba(53,48,122,0) 0%,rgba(53,48,122,.55) 35%,rgba(53,48,122,.8) 100%);
    clip-path:polygon(46% 0,54% 0,60% 40%,80% 75%,100% 100%,0 100%,20% 75%,40% 40%)}
  .ground-band{position:absolute;left:0;right:0;bottom:0;height:40px;background:var(--navy-light);opacity:.7}
  .panel-content{position:relative;padding:0 36px}
  .brand{text-align:center;padding-top:50px}
  .brand-mark{display:block;width:22px;height:22px;background:var(--ink);margin:0 auto 14px}
  .brand-name{font-family:"Saira Semi Condensed",sans-serif;font-size:10px;letter-spacing:6px;text-transform:uppercase}
  .section-title{font-family:"Allura",cursive;color:var(--red);font-weight:400;line-height:1;white-space:nowrap;text-align:center;font-size:48px;margin-left:-16px;margin-right:-16px}
  .panel--brunch .section-title{margin-top:56px;margin-bottom:34px}
  .panel--drinks .section-title{margin-top:38px;margin-bottom:34px}
  .menu-item{margin-bottom:12px}
  .item-head{display:flex;align-items:center;height:20px;margin-bottom:4px}
  .item-icon{width:19px;height:19px;background:var(--icon-bg);border-radius:2px;display:flex;align-items:center;justify-content:center;margin-right:5px;flex:none}
  .item-name{font-weight:700;color:var(--red);font-size:14.5px;flex:1;line-height:1}
  .item-price{background:var(--badge);color:var(--ink);font-weight:600;font-size:11.5px;padding:1px 4px;border-radius:2px;line-height:14px}
  .item-desc{font-size:10.6px;line-height:14.2px;font-weight:400}
</style>
</head>
<body>
  <svg width="0" height="0" style="position:absolute">
    <symbol id="cloche" viewBox="0 0 20 20">
      <circle cx="10" cy="5" r="1.2" fill="#4d4b6e"/>
      <path d="M3 13a7 7 0 0 1 14 0z" fill="#4d4b6e"/>
      <rect x="2" y="14" width="16" height="1.6" fill="#4d4b6e"/>
    </symbol>
  </svg>

  <section class="panel panel--brunch">
    <div class="tower-silhouette" role="img" aria-label="Faint Eiffel Tower silhouette in the background"></div>
    <div class="ground-band"></div>
    <div class="panel-content">
      <header class="brand">
        <div class="brand-mark"></div>
        <div class="brand-name">Miel du Matin</div>
      </header>
      <h1 class="section-title">Brunch Specials</h1>

      <article class="menu-item">
        <div class="item-head"><span class="item-icon"><svg width="15" height="15"><use href="#cloche"/></svg></span><h2 class="item-name">Ratatouille &amp; Eggs</h2><span class="item-price">$18</span></div>
        <p class="item-desc">Experience the essence of Provence with our Ratatouille, a vibrant medley of roasted squash, peppers, tomatoes, eggplant, infused with fragrant fresh herbs. Served with two perfectly poached eggs, and your choice of flavorful andouille sausage or crispy bacon. Accompanied by a side of crusty baguette. It's a hearty dish that celebrates the flavors of the Mediterranean countryside.</p>
      </article>
      <article class="menu-item">
        <div class="item-head"><span class="item-icon"><svg width="15" height="15"><use href="#cloche"/></svg></span><h2 class="item-name">Le Grande Breakfast</h2><span class="item-price">$15</span></div>
        <p class="item-desc">Start your day in style with our Le Grande Breakfast, a feast fit for royalty. Customize your morning indulgence with two eggs cooked to your preference, paired with either savory bacon or succulent chicken sausage. Choose between a freshly baked baguette or a buttery croissant to accompany your meal. Complete your breakfast by selecting from an array of sides including crispy hash browns, savory roasted potatoes, or a refreshing fruit salad. Bon appetit!</p>
      </article>
      <article class="menu-item">
        <div class="item-head"><span class="item-icon"><svg width="15" height="15"><use href="#cloche"/></svg></span><h2 class="item-name">Smoked Salmon Tartine</h2><span class="item-price">$14</span></div>
        <p class="item-desc">Delight in the luxurious flavors of our Smoked Salmon Tartine, a culinary masterpiece that elevates breakfast to new heights. Indulge in truffled scrambled eggs nestled atop smoked salmon, adorned with tangy pickled red onions, briny caper berries, crisp cucumber, juicy tomato, and peppery arugula. All artfully arranged on multigrain bread generously spread with herb-infused cream cheese.</p>
      </article>
      <article class="menu-item">
        <div class="item-head"><span class="item-icon"><svg width="15" height="15"><use href="#cloche"/></svg></span><h2 class="item-name">Le Benedict Salmon</h2><span class="item-price">$14</span></div>
        <p class="item-desc">Savor the classic elegance of Eggs Benedict, featuring two perfectly poached eggs nestled on toasted English muffins, with luscious smoked salmon and ripe tomato slices crowned with a velvety lemon-infused Hollandaise sauce. A timeless brunch delight crafted to perfection.</p>
      </article>
      <article class="menu-item">
        <div class="item-head"><span class="item-icon"><svg width="15" height="15"><use href="#cloche"/></svg></span><h2 class="item-name">Salmon Atlantique</h2><span class="item-price">$14</span></div>
        <p class="item-desc">Enjoy a bed of crisp mixed greens adorned with delicate smoked salmon, sweet golden raisins, creamy goat cheese, and crunchy walnuts. All dressed in a tantalizing balsamic vinaigrette that ties the elements together perfectly.</p>
      </article>
      <article class="menu-item">
        <div class="item-head"><span class="item-icon"><svg width="15" height="15"><use href="#cloche"/></svg></span><h2 class="item-name">Beef Bourguignon</h2><span class="item-price">$18</span></div>
        <p class="item-desc">Indulge in our rich and comforting flavors of savory, tender beef slowly braised in red wine, creating a luscious sauce that envelops pearl onions, carrots, and mushrooms in a symphony of flavors. Served alongside buttered egg noodles. It's a hearty and soul-warming meal that promises pure culinary bliss.</p>
      </article>
      <article class="menu-item">
        <div class="item-head"><span class="item-icon"><svg width="15" height="15"><use href="#cloche"/></svg></span><h2 class="item-name">Tourte au Poulet</h2><span class="item-price">$15</span></div>
        <p class="item-desc">Discover the indulgent flavors of our Tourte au Poulet, a savory delight that marries tender marinated chicken with the richness of Swiss cheese and the sweetness of onions, all encased in layers of flaky pastry. Topped with a savory mushroom medley and decadent bechamel sauce. A true comfort classic to delight your senses.</p>
      </article>
    </div>
  </section>

  <section class="panel panel--drinks">
    <div class="tower-silhouette" role="img" aria-label="Faint Eiffel Tower silhouette in the background"></div>
    <div class="ground-band"></div>
    <div class="panel-content">
      <h1 class="section-title">Drink Specials</h1>

      <article class="menu-item">
        <div class="item-head"><span class="item-icon"><svg width="15" height="15"><use href="#cloche"/></svg></span><h2 class="item-name">Bottomless Mimosa</h2><span class="item-price">$18</span></div>
        <p class="item-desc">Embark on an endless journey of delight with our Bottomless Mimosa, featuring Westbrook champagne, infusing each sip with a sparkling sensation. Tailor your experience with your preferred flavor profile - opt for the timeless twist of classic orange juice or tangy cranberry juice for a refreshing zing. Continuously poured to ensure your glass is always full.</p>
      </article>
      <article class="menu-item">
        <div class="item-head"><span class="item-icon"><svg width="15" height="15"><use href="#cloche"/></svg></span><h2 class="item-name">Apple Cider-Mimosa</h2><span class="item-price">$9</span></div>
        <p class="item-desc">A delightful twist on the classic mimosa. Crafted with champagne and crisp apple cider. To elevate the experience, we adorn the glass with a caramel rim dipped in brown sugar, adding a touch of indulgent sweetness to every sip.</p>
      </article>
      <article class="menu-item">
        <div class="item-head"><span class="item-icon"><svg width="15" height="15"><use href="#cloche"/></svg></span><h2 class="item-name">Blood Orange or Pineapple Spritz</h2><span class="item-price">$12</span></div>
        <p class="item-desc">Introducing our vibrant spritz cocktail, a tantalizing blend of Tolland &amp; Blend premium Varenka Vodka, sweet vermouth, and a touch of sweetness from a carefully muddled sugar cube. This effervescent libation reaches new heights with the addition of bubbly Fontaine, your choice of either Blood Orange or Pineapple syrup injects a burst of fruity allure into every sip.</p>
      </article>
      <article class="menu-item">
        <div class="item-head"><span class="item-icon"><svg width="15" height="15"><use href="#cloche"/></svg></span><h2 class="item-name">Peach Bellini</h2><span class="item-price">$9</span></div>
        <p class="item-desc">Try our perfectly balanced Peach Bellini with each sip you capture the crispness of champagne with the irresistible sweetness of peach. It's a sublime fusion of sophistication and sweetness.</p>
      </article>
      <article class="menu-item">
        <div class="item-head"><span class="item-icon"><svg width="15" height="15"><use href="#cloche"/></svg></span><h2 class="item-name">Espresso Martini</h2><span class="item-price">$10</span></div>
        <p class="item-desc">Our Espresso Martini is a decadent blend of bold espresso, rich chocolate martini, and luxurious Castellani chocolate syrup. It's the ultimate indulgence for coffee and chocolate lovers alike.</p>
      </article>
      <article class="menu-item">
        <div class="item-head"><span class="item-icon"><svg width="15" height="15"><use href="#cloche"/></svg></span><h2 class="item-name">Kir Royale</h2><span class="item-price">$10</span></div>
        <p class="item-desc">Our Kir Royale is a delightful fusion of the crisp, sparkling champagne bubbles and the sweet sophistication of black currant. a luxurious and indulgent drink that's perfect for any occasion.</p>
      </article>
      <article class="menu-item">
        <div class="item-head"><span class="item-icon"><svg width="15" height="15"><use href="#cloche"/></svg></span><h2 class="item-name">Latte Truffle Latte</h2><span class="item-price">$6</span></div>
        <p class="item-desc">We start with rich Castellani chocolate, known for its velvety smoothness and intense flavor. Then, we add a drizzle of salted caramel, adding a perfect balance of sweetness and a hint of savory richness. Finally, we combine this delightful blend with perfectly steamed milk to create a creamy and indulgent latte that will satisfy even the most discerning palate.</p>
      </article>
      <article class="menu-item">
        <div class="item-head"><span class="item-icon"><svg width="15" height="15"><use href="#cloche"/></svg></span><h2 class="item-name">Napoleon Latte</h2><span class="item-price">$6</span></div>
        <p class="item-desc">We start with rich Castellani chocolate, known for its velvety smoothness and intense flavor. Then, we add a drizzle of salted caramel, adding a perfect balance of sweetness and a hint of savory richness. Finally, we combine this delightful blend with perfectly steamed milk to create a creamy and indulgent latte that will satisfy even the most discerning palate.</p>
      </article>
      <article class="menu-item">
        <div class="item-head"><span class="item-icon"><svg width="15" height="15"><use href="#cloche"/></svg></span><h2 class="item-name">Chai Latte</h2><span class="item-price">$6</span></div>
        <p class="item-desc">Our robust chai tea concentrate, infused with a symphony of cinnamon, cardamom, cloves, and ginger, sets the stage for a journey of aromatic delight. Paired with velvety steamed milk, each sip offers a harmonious blend of bold spices and creamy richness. Topped with a sprinkle of cinnamon, it's the perfect finishing touch to this comforting treat.</p>
      </article>
    </div>
  </section>
</body>
</html>
```